Business Card Design

We are a commercial real estate brokerage in San Francisco, leasing office buildings downtown.
I would like a clean, elegant look. Simple but powerful .

Industry/Entity Type

Business

Contact Information for Business Card

Colin Farrow
lic# 07281549
415.555.0172
colin@tarvo-commercial.example
tarvo-commercial.example

```html
<!DOCTYPE html>
<html lang="en">
<head>
<meta charset="UTF-8">
<title>Tarvo Commercial – Business Card</title>
<link rel="stylesheet" href="https://fonts.googleapis.com/css2?family=Jost:wght@400;500&display=swap">
<style>
  :root {
    --bg: #ececec;
    --card: #ffffff;
    --slate: #4a505b;
    --ink-black: #1f1f21;
    --mist: #b3bbcc;
    --text: #222326;
    --icon: #3d4048;
  }
  * { margin: 0; padding: 0; box-sizing: border-box; }
  html, body {
    width: 1200px; height: 799px; overflow: hidden;
    background: var(--bg);
    font-family: "Jost", sans-serif;
  }
  .card {
    position: absolute; left: 100px; top: 119px;
    width: 1000px; height: 561px;
    background: var(--card);
    overflow: hidden;
  }
  .card-shapes { position: absolute; inset: 0; width: 100%; height: 100%; }
  .shape-slate { fill: var(--slate); }
  .shape-black { fill: var(--ink-black); }
  .shape-mist { fill: var(--mist); }

  .brand {
    position: absolute; left: 420px; top: 96px;
    display: flex; align-items: center; gap: 20px;
  }
  .brand-mark { width: 56px; height: 56px; background: var(--slate); flex: none; }
  .brand-name {
    color: var(--text); font-weight: 500; font-size: 44px;
    line-height: 1; white-space: nowrap;
  }

  .contact { position: absolute; color: var(--text); display: flex; align-items: center; white-space: nowrap; }
  .contact svg { fill: var(--icon); flex: none; }
  .person { left: 376px; top: 228px; font-size: 40px; font-weight: 500; }
  .person svg { width: 28px; height: 28px; margin-right: 18px; }
  .license { position: absolute; left: 420px; top: 280px; font-size: 31px; color: var(--text); }
  .web { left: 346px; top: 338px; font-size: 28px; }
  .phone { left: 324px; top: 406px; font-size: 28px; }
  .email { left: 300px; top: 476px; font-size: 27px; }
  .web svg, .phone svg, .email svg { width: 30px; height: 30px; margin-right: 14px; }
</style>
</head>
<body>
  <main class="card">
    <svg class="card-shapes" viewBox="0 0 485 272" preserveAspectRatio="none" aria-hidden="true">
      <polygon class="shape-mist" points="176,0 193,0 102,272 86,272"/>
      <polygon class="shape-slate" points="0,0 180,0 90,272 0,272"/>
      <polygon class="shape-black" points="0,67 92,272 0,272"/>
      <polygon class="shape-mist" points="475,0 485,0 485,272 370,272"/>
      <polygon class="shape-slate" points="485,87 485,272 385,272"/>
    </svg>

    <div class="brand">
      <div class="brand-mark"></div>
      <div class="brand-name">Tarvo Commercial</div>
    </div>

    <div class="contact person">
      <svg viewBox="0 0 24 24"><circle cx="12" cy="7" r="5"/><path d="M2 23c0-6 4.5-9 10-9s10 3 10 9z"/></svg>
      <span>Colin Farrow</span>
    </div>
    <div class="license">lic# 07281549</div>

    <div class="contact web">
      <svg viewBox="0 0 24 24"><path d="M12 1a11 11 0 100 22 11 11 0 000-22zm7.9 10h-3.4a17 17 0 00-1.6-7.2A9 9 0 0119.9 11zM12 3.2c1.2 1.5 2.3 4.3 2.5 7.8h-5C9.7 7.5 10.8 4.7 12 3.2zM9.1 3.8A17 17 0 007.5 11H4.1a9 9 0 015-7.2zM4.1 13h3.4a17 17 0 001.6 7.2 9 9 0 01-5-7.2zm7.9 7.8c-1.2-1.5-2.3-4.3-2.5-7.8h5c-.2 3.5-1.3 6.3-2.5 7.8zm2.9-.6a17 17 0 001.6-7.2h3.4a9 9 0 01-5 7.2z"/></svg>
      <span>tarvo-commercial.example</span>
    </div>

    <div class="contact phone">
      <svg viewBox="0 0 24 24"><path d="M6.6 10.8a15.1 15.1 0 006.6 6.6l2.2-2.2a1 1 0 011-.25 11.4 11.4 0 003.6.57 1 1 0 011 1V20a1 1 0 01-1 1A17 17 0 013 4a1 1 0 011-1h3.5a1 1 0 011 1c0 1.250.2 2.45.57 3.57a1 1 0 01-.25 1z"/></svg>
      <span>415.555.0172</span>
    </div>

    <div class="contact email">
      <svg viewBox="0 0 24 24"><path d="M2 5h20v2l-10 6L2 7z"/><path d="M2 9l10 6 10-6v10H2z"/></svg>
      <span>colin@tarvo-commercial.example</span>
    </div>
  </main>
</body>
</html>
```